依頼詳細
イラスト(写真枠なし)、写真枠入りのデザインを依頼します。
用途は2015年の年賀状用です。

1つのデザインに対して使用できる写真の枚数枠は1枚~5枚です。
タテ型1点もしくはヨコ型1点でご提案下さい。
(提案されるデザインがイラストタイプなのか、写真入りタイプなのか、また写真枠の数についてはお任せいたします。)

デザインを作成するにあたって

・ユーザーは子供の写真や家族関係が多いです。
・写真が主役なのでその点を考慮の上、デザイン下さい。
・定番のタイプから家族向けのやさしいタイプのものまで幅広く、募集します。

複数採用予定ですので同じ方でも複数のデザインを提案して頂いても構いません。
こちらの希望に合致しましたデザイナー様は今後も別途、ご依頼させて頂ければと考えております。
デザインのテンプレートの作成仕様及びPSDの雛形については添付ファイルを参照して下さい。

添付資料を必ず、読んでください。
添付資料の条件から外れたデザインにつきましては、どんなに良いデザインでも採用できません(システム上)のでご注意下さい。
記載項目
はがきサイズ

詳細は添付資料でご確認下さい。
補足でデザインの外枠部分にデザインがかかる場合は裁ち落とし時にカットされるおそれがございます。
デザインがカットされない様に余白にしたり、塗り足し等で調整して下さい。
その点を考慮して、デザイン作成して下さい。
希望イメージ
シンプル 複雑
単色 カラフル
暗い 明るい
日常 高級
遊び心 厳粛
未来的 伝統的
女性的 男性的
希望する色
特にありませんが明るめの感じでお願いします。
納品ファイル
• フォトショップ形式 (.psd)
補足説明
デザインはオリジナルの物のみとします。(同じデザインの色違い等の提案もOKです。)
採用作品デザインの使用・販売に関する権利は弊社のものとさせて頂き、弊社での商用利用に使用させて頂きます。
契約が成立した場合でも盗作等が発覚した場合や他でも同じデザインが使用されている等が発覚した場合は契約を破棄させて頂きます。

添付資料の住所枠(サイズも含めて)については必須でお願いしますが挨拶文枠は設けて頂かなくても構いません。

また今回は1点だけでなく計1~100点の募集となります。
契約成立の金額は下記金額となります。
全応募デザインより弊社にてランク付けさせて頂き、上位1位の方には5万円、以下1万円〜500円迄の報酬となります。
※デザインのクオリティーや弊社の希望に沿わないデザインが多い場合は上記の募集以下での採用になる場合がございます。
予め、ご了承下さい。

1位 5万円
2~5位 1万円
6~10位 5千円
11~50位 1000円
51~100位 500円
ご連絡が遅れてすみません。
この度は多数の素敵なデザインを作成頂きまして誠にありがとうございます。
現在、弊社スタッフで選定及び順位付け作業を行っております。
今週中には作業完了予定です。
当選の連絡につきましては週末及び週明けまでにご連絡させて頂きますので今、暫くお待ち頂ければ幸いです。
以上、ご連絡申し上げます。
■ 選んだ理由

たくさんのデザイナー様から素敵なデザインを提案頂きましたが社内で色々と検討した結果、こちらのデザインをトップに選定させて頂く事になりました。
理由はかわいらしさもありながら正月っぽいデザインが気に入りました。

■ 提案者全員のお礼・コメント

この度は多数の素敵なデザインを作成頂きまして誠にありがとうございました。
お陰様で複数の採用をさせて頂きました。
別途、選定させて頂いたデザイナー様には連絡をさせて頂いておりますので、もしよろしければ使用させて頂ければ幸いです。
改めて御礼申し上げます。

```html
<!DOCTYPE html>
<html lang="ja">
<head>
<meta charset="utf-8">
<title>年賀状 写真フレーム</title>
<link rel="stylesheet" href="https://fonts.googleapis.com/css2?family=M+PLUS+Rounded+1c&display=swap">
<style>
  :root {
    --paper: #ffffff;
    --frame-line: #f0b8c8;
    --photo-grey: #b5b1b2;
    --wreath-pink: #f7a8c8;
    --wreath-yellow: #fbe06a;
    --wreath-lilac: #d7b2f2;
    --wreath-mint: #b8ecc4;
    --wreath-sky: #bfe8f6;
    --sheep-peach: #f7d2bf;
    --sheep-lemon: #f8ef9e;
    --sheep-rose: #f5a9c4;
  }
  html, body {
    margin: 0;
    padding: 0;
    overflow: hidden;
  }
  body {
    width: 805px;
    height: 1200px;
    background: var(--paper);
    font-family: "M PLUS Rounded 1c", sans-serif;
  }
  .card {
    position: relative;
    width: 805px;
    height: 1200px;
    background: var(--paper);
  }
  .message-box,
  .address-box {
    position: absolute;
    border: 2px solid var(--frame-line);
    box-sizing: border-box;
    background: var(--paper);
  }
  .message-box { left: 67px; top: 40px; width: 676px; height: 102px; }
  .address-box { left: 429px; top: 813px; width: 349px; height: 346px; }
  .wreath {
    position: absolute;
    border-radius: 50%;
    background: conic-gradient(var(--wreath-pink), var(--wreath-yellow), var(--wreath-lilac), var(--wreath-mint), var(--wreath-sky), var(--wreath-pink));
    opacity: 0.85;
  }
  .wreath--main { left: 143px; top: 156px; width: 600px; height: 600px; }
  .wreath--small { left: 22px; top: 786px; width: 332px; height: 332px; }
  .photo-slot {
    position: absolute;
    border-radius: 50%;
    background: var(--photo-grey);
  }
  .photo-slot--main { left: 223px; top: 236px; width: 440px; height: 440px; }
  .photo-slot--small { left: 54px; top: 818px; width: 268px; height: 268px; }
  .sheep {
    position: absolute;
    border-radius: 45%;
  }
  .sheep--peach { left: 50px; top: 175px; width: 98px; height: 75px; background: var(--sheep-peach); }
  .sheep--lemon { left: 670px; top: 160px; width: 100px; height: 78px; background: var(--sheep-lemon); }
  .sheep--rose { left: 105px; top: 690px; width: 95px; height: 70px; background: var(--sheep-rose); }
</style>
</head>
<body>
  <main class="card">
    <div class="message-box" aria-label="挨拶文欄"></div>

    <div class="wreath wreath--main" role="img" aria-label="カラフルな花のリース"></div>
    <div class="photo-slot photo-slot--main" role="img" aria-label="写真枠(大)"></div>

    <div class="wreath wreath--small" role="img" aria-label="カラフルな花のリース(小)"></div>
    <div class="photo-slot photo-slot--small" role="img" aria-label="写真枠(小)"></div>

    <div class="sheep sheep--peach" role="img" aria-label="ピーチ色の羊のイラスト"></div>
    <div class="sheep sheep--lemon" role="img" aria-label="黄色の羊のイラスト"></div>
    <div class="sheep sheep--rose" role="img" aria-label="ピンクの羊のイラスト"></div>

    <div class="address-box" aria-label="差出人住所欄"></div>
  </main>
</body>
</html>
```